Motor Mate 4x6 Flyer

Need 4 x 6 Flyer with following language:

Willow Crest Motor Mate
Our Motor Mate Will Come to Your Home
Our Motor Mate will Drive Your Car to Nearest Gas Station
Our Motor Mate will Fill-up Your Car with Gas
Our Motor Mate will Immediately Return Your Car
Your Car Covered with $100k of Commercial Insurance
Member Dunmore Chamber of Commerce / Honest Merchant League
www.willowcrestmotormate.example

Place logos of Vortan, Brenn & Dorvane on Left Side of Flyer starting at top left corner, mid left side, left bottom corner.
Place logos of BoltNest, 12-Forty, Tesmira on opposite side right.....
Place Willow Crest Motor Mate Logo on both sides of very top that says Willow Crest Motor Mate

Target Market(s)

Upscale Home Owners

Font styles to use
Sans Serif

Colors
F0912C
F2A743
F7CA91
FBE8D2
FDF5EE

Requirements
Must have
• Flyer Must be Bright Orange

```html
<!DOCTYPE html>
<html lang="en">
<head>
<meta charset="utf-8">
<title>Willow Crest Motor Mate – Flyer</title>
<link rel="stylesheet" href="https://fonts.googleapis.com/css2?family=Mulish:wght@800;900&family=Oswald:wght@500&family=Roboto:wght@500&family=Ubuntu:wght@500;700&display=swap">
<style>
  :root {
    --orange-deep: #f37321;
    --orange: #f0912c;
    --orange-mid: #f2a743;
    --orange-soft: #f7ca91;
    --cream: #fbe8d2;
    --paper: #fdf5ee;
    --light-grey: #eeeeee;
    --ink: #2b2b2b;
    --black: #0a0a0a;
    --white: #ffffff;
    --accent-red: #e1262c;
    --line-yellow: #ffd400;
    --backdrop: #5e6064;
  }
  * { box-sizing: border-box; margin: 0; padding: 0; }
  html, body { width: 1178px; height: 1200px; overflow: hidden; }
  body { background: var(--backdrop); position: relative; }

  .flyer {
    position: absolute; left: 201px; top: 19px;
    width: 776px; height: 1162px; overflow: hidden;
    background: linear-gradient(180deg, var(--orange-mid) 0%, #f4ab4a 60%, var(--orange-mid) 100%);
    font-family: "Ubuntu", sans-serif;
  }
  .header-panel {
    position: absolute; left: 0; top: 54px; width: 100%; height: 376px;
    background: linear-gradient(160deg, var(--white) 0%, var(--paper) 45%, #ececec 100%);
  }
  .header-edge { position: absolute; left: 0; top: 0; }

  .site-url {
    position: absolute; right: 36px; top: 20px;
    color: var(--white); font-weight: 700; font-size: 26px; letter-spacing: 1px;
  }
  .brand-tab-name {
    position: absolute; left: 329px; width: 405px; top: 76px;
    text-align: center; color: var(--white); font-weight: 700; font-size: 29px;
  }

  .brand-mark {
    position: absolute; left: 136px; top: 110px; width: 68px; height: 68px;
    background: var(--accent-red); border-radius: 8px;
  }
  .brand-name {
    position: absolute; left: 18px; width: 310px; top: 226px;
    text-align: center; font-weight: 500; font-size: 40px; color: var(--ink);
    letter-spacing: 0.5px; white-space: nowrap;
  }
  .divider { position: absolute; left: 343px; top: 140px; width: 2px; height: 140px; background: #bdbdbd; }

  .headline {
    position: absolute; left: 370px; top: 150px; width: 356px;
    font-family: "Mulish", sans-serif; font-weight: 900; font-size: 35px; line-height: 39px;
    color: var(--ink); letter-spacing: -0.8px; white-space: nowrap;
  }
  .headline .hot { color: var(--orange-deep); }

  .guide { position: absolute; background: var(--line-yellow); }
  .guide-right { left: 734px; top: 118px; width: 2px; height: 775px; }
  .guide-left { left: 38px; top: 801px; width: 2px; height: 92px; }
  .guide-base { left: 38px; top: 891px; width: 698px; height: 2px; }

  .photo-frame {
    position: absolute; left: 170px; top: 308px; width: 439px; height: 498px;
    background: var(--black);
  }
  .photo {
    position: absolute; left: 17px; top: 18px; width: 405px; height: 402px;
    background: linear-gradient(135deg, #6f9a3c 0%, #a6c36a 30%, #4d6f9a 55%, #e3b52a 100%);
  }
  .photo-caption {
    position: absolute; left: 0; width: 100%; top: 428px;
    text-align: center; color: var(--white);
    font-family: "Roboto", sans-serif; font-weight: 500; font-size: 25px; line-height: 29px;
  }

  .service-line {
    position: absolute; left: 40px; width: 694px; text-align: center;
    font-weight: 700; font-size: 24px; color: var(--black); white-space: nowrap;
  }
  .service-fill { top: 813px; }
  .service-return { top: 853px; }
  .service-rule { position: absolute; left: 87px; top: 849px; width: 598px; height: 1px; background: var(--orange-deep); }

  .partner-strip {
    position: absolute; left: 38px; top: 893px; width: 698px; height: 93px;
    background: linear-gradient(180deg, #f4f4f4, #dedede);
    display: flex; align-items: center;
  }
  .partner {
    flex: 1; text-align: center; font-weight: 700; font-size: 22px;
    border-right: 1px solid #c9c9c9; line-height: 60px; white-space: nowrap;
  }
  .partner:last-child { border-right: none; }
  .partner-vortan { color: var(--accent-red); font-size: 27px; }
  .partner-brenn { color: #d8262c; }
  .partner-dorvane { color: #1b5faa; }
  .partner-boltnest { color: #222222; border-left: 3px solid var(--accent-red); }
  .partner-twelve { color: #008a4b; }
  .partner-tesmira { color: #00758d; }

  .membership {
    position: absolute; left: 0; width: 100%; top: 996px; text-align: center;
    font-family: "Oswald", sans-serif; font-weight: 500; font-size: 27px; color: var(--black);
    white-space: nowrap;
  }

  .insurance-band { position: absolute; left: 0; top: 1050px; width: 776px; height: 112px; }
  .insurance-text {
    position: absolute; left: 0; width: 100%; top: 1064px; text-align: center;
    color: var(--white); font-weight: 700; font-size: 36px; line-height: 40px;
  }
</style>
</head>
<body>
  <main class="flyer">
    <div class="header-panel"></div>

    <svg class="header-edge" width="776" height="130" viewBox="0 0 776 130" aria-hidden="true">
      <rect x="0" y="0" width="776" height="54" fill="var(--orange-deep)"/>
      <polygon points="0,54 268,54 290,68 0,68" fill="var(--cream)"/>
      <polygon points="268,54 776,54 776,68 290,68" fill="var(--orange-deep)"/>
      <path d="M329,68 L734,68 L716,104 Q708,120 690,120 L370,120 Q352,120 344,104 Z" fill="#2e2e2e"/>
    </svg>

    <p class="site-url">www.willowcrestmotormate.example</p>
    <p class="brand-tab-name">Willow Crest Motor Mate</p>

    <div class="brand-mark"></div>
    <p class="brand-name">MOTOR MATE</p>
    <div class="divider"></div>

    <h1 class="headline">
      OUR MOTOR MATE<br>
      WILL <span class="hot">COME TO</span><br>
      <span class="hot">YOUR HOME</span>
    </h1>

    <div class="guide guide-right"></div>
    <div class="guide guide-left"></div>

    <figure class="photo-frame">
      <div class="photo" role="img" aria-label="Photo of a smiling woman in a denim shirt refuelling a blue car at a gas pump, trees in the background"></div>
      <figcaption class="photo-caption">Our Motor Mate will Drive Your<br>Car to Nearest Gas Station</figcaption>
    </figure>

    <p class="service-line service-fill">Our Motor Mate will Fill-up Your Car with Gas</p>
    <div class="service-rule"></div>
    <p class="service-line service-return">Our Motor Mate will Immediately Return Your Car</p>

    <div class="guide guide-base"></div>
    <div class="partner-strip">
      <span class="partner partner-vortan">Vortan</span>
      <span class="partner partner-brenn">Brenn</span>
      <span class="partner partner-dorvane">Dorvane</span>
      <span class="partner partner-boltnest">BoltNest</span>
      <span class="partner partner-twelve">12-Forty</span>
      <span class="partner partner-tesmira">Tesmira</span>
    </div>

    <p class="membership">Member Dunmore Chamber of Commerce / Honest Merchant League</p>

    <svg class="insurance-band" viewBox="0 0 776 112" preserveAspectRatio="none" aria-hidden="true">
      <path d="M0,8 L60,4 L140,9 L260,3 L420,8 L560,2 L680,7 L776,3 L776,112 L0,112 Z" fill="var(--black)"/>
    </svg>
    <p class="insurance-text">Your Car Covered with<br>$100k of Commercial Insurance</p>
  </main>
</body>
</html>
```